CalmHaven Webpage for Integrative and Holistic Psychiatric Practice

We need a webpage designed for a medical practice that focuses on integrative and holistic psychiatry. We focus on providing care to mothers and families. The name of the company is Calm Haven, incorporated, A Professional Medical Corporation.

We'd like the color palette to be earthy/natural with the same look and feel as our logo that's attached. We're not set on anything, so feel free to have fun with the palette. We just want it to be warm and inviting in particular for Moms!

We'd like to have our logo in the top left with links below it either centered or to the right. We really like websites like http://www.brightmeadowclinic.example/home.html and http://www.tarnwickmindpartners.example/site/ to give you an idea of what we're looking for.

For links, we're looking for the following. Dummy text is fine, we're still getting content together:

* Home
* About Us - this page would have headings for Directions, Staff, Appointment Scheduling
* Services Provided - headings for 8 different services
* Patient Resources - headings for Patient Forms, Fees, Articles
* FAQ
* Contact Us

The webpage will be hosted as an Office 365 Public Website, so feel free to use whatever SharePoint integration you would like, but it's not necessary.

Thank you!

```html
<!DOCTYPE html>
<html lang="en">
<head>
<meta charset="utf-8">
<title>CalmHaven — A Professional Medical Corporation</title>
<link rel="stylesheet" href="https://fonts.googleapis.com/css2?family=Open+Sans:wght@300;400;600;700&display=swap">
<style>
  :root{
    --brown:#5b2c0a;
    --brown-dark:#4a2206;
    --nav:#6b3409;
    --green:#2f5e0b;
    --green-dark:#1f4205;
    --text:#6d6d6d;
    --muted:#9a9a9a;
    --field:#f1f1f1;
    --band:#f7f7f7;
    --page:#efefef;
  }
  *{box-sizing:border-box;margin:0;padding:0}
  html,body{width:1199px;height:1200px;overflow:hidden}
  body{
    font-family:"Open Sans",Arial,sans-serif;
    background:#fff;
    position:relative;
    color:var(--text);
  }
  .top-band{
    position:absolute;left:0;top:0;width:1199px;height:492px;
    background-color:var(--page);
    background-image:linear-gradient(rgba(255,255,255,.55) 1px,transparent 1px),linear-gradient(90deg,rgba(255,255,255,.55) 1px,transparent 1px);
    background-size:3px 3px;
  }
  .column{
    position:absolute;left:170px;top:492px;width:856px;height:708px;
    background:#fff;box-shadow:0 0 6px rgba(0,0,0,.08);
  }
  .brand{position:absolute;left:174px;top:62px;display:flex;align-items:center;gap:12px}
  .brand-dot{width:34px;height:34px;border-radius:50%;background:var(--green)}
  .brand-name{font-size:34px;font-weight:600;color:var(--brown)}
  .search{
    position:absolute;left:836px;top:16px;width:190px;height:30px;border-radius:15px;
    background:#e8e8e8;font-size:13px;color:var(--muted);padding:6px 15px;
  }
  .search svg{position:absolute;right:12px;top:8px}
  .contact{
    position:absolute;right:173px;top:63px;display:flex;gap:20px;
    font-size:22px;font-weight:600;color:var(--brown);white-space:nowrap;
  }
  .contact span{display:flex;align-items:center;gap:8px}
  .nav{
    position:absolute;left:398px;top:111px;width:628px;height:43px;
    background:var(--nav);border-radius:6px;display:flex;align-items:center;
    box-shadow:0 2px 0 var(--brown-dark);
  }
  .nav a{
    color:#fff;text-decoration:none;font-size:13px;font-weight:600;
    height:43px;line-height:43px;padding:0 15px;white-space:nowrap;flex:none;
  }
  .nav a.active{background:var(--brown-dark);border-radius:6px;width:105px;text-align:center;padding:0}
  .hero{
    position:absolute;left:170px;top:172px;width:856px;height:320px;border-radius:6px;
    border:1px solid var(--brown);overflow:hidden;
    background:linear-gradient(180deg,#cfd9e2 0%,#e7ecef 45%,#b9c6cf 70%,#d9cbb5 100%);
  }
  .hero-title{
    position:absolute;left:516px;top:50px;width:350px;text-align:center;
    font-size:34px;line-height:39px;font-weight:700;color:var(--brown);
  }
  .btn{
    display:block;border-radius:6px;color:#fff;font-weight:600;text-align:center;text-decoration:none;
  }
  .hero-btn{
    position:absolute;left:740px;top:373px;width:242px;height:41px;line-height:41px;
    background:var(--brown-dark);font-size:13px;box-shadow:0 3px 0 #2e1403;white-space:nowrap;
  }
  .dots{position:absolute;display:flex;gap:2px}
  .dots i{width:11px;height:11px;border-radius:50%;background:#d9d0c5}
  .hero-dots{left:837px;top:444px}
  .hero-dots i.on{background:var(--brown-dark)}
  .welcome{position:absolute;left:185px;top:533px;width:535px}
  .welcome h1{font-size:30px;font-weight:300;color:var(--brown);margin-bottom:18px;white-space:nowrap}
  .welcome h1 strong{font-weight:700;color:var(--green)}
  .welcome p{font-size:12.5px;line-height:15px;color:var(--text);margin-bottom:14px}
  .appointment{position:absolute;left:756px;top:533px;width:257px}
  .appointment h2{font-size:27px;font-weight:600;color:var(--brown);margin-bottom:10px}
  .field{
    position:relative;background:var(--field);font-size:11px;color:#b2b2b2;
    padding:10px 10px;height:32px;margin-bottom:4px;
  }
  .field.message{height:83px}
  .field svg{position:absolute;right:9px;top:9px}
  .send{
    position:absolute;left:154px;top:207px;width:103px;height:34px;line-height:34px;
    background:var(--green);font-size:14px;font-weight:700;box-shadow:0 3px 0 var(--green-dark);
  }
  .news{position:absolute;left:170px;top:828px;width:856px;height:261px;background:var(--band)}
  .news h2{position:absolute;left:15px;top:32px;font-size:26px;font-weight:600;color:var(--green)}
  .news-dots{left:794px;top:45px}
  .news-dots i{background:#ddd}
  .news-dots i.on{background:var(--green)}
  .card{position:absolute;top:82px;width:270px;height:158px}
  .card-1{left:15px;background:linear-gradient(90deg,#e9ecef,#c9d3dc 60%,#e7dccf)}
  .card-2{left:294px;background:linear-gradient(135deg,#a3b77c,#c6d0a5);display:flex;flex-direction:column;align-items:center;padding-top:28px;color:#fff;text-align:center}
  .card-3{left:574px;background:linear-gradient(90deg,#f2f4f7,#aebfd9 50%,#eef0f3)}
  .card-2 h3{font-size:16px;font-weight:600;margin:4px 0 3px}
  .card-2 p{font-size:10.5px;line-height:12px;width:250px}
  .footer{position:absolute;left:170px;top:1128px;width:856px;text-align:center;font-size:10.5px;color:#888}
  .social{display:flex;justify-content:center;gap:8px;margin-top:6px}
  .social i{width:19px;height:19px;border-radius:50%;background:#b5b5b5}
</style>
</head>
<body>
  <div class="top-band"></div>
  <div class="column"></div>

  <header>
    <div class="brand"><span class="brand-dot"></span><span class="brand-name">CalmHaven</span></div>
    <div class="search">Search
      <svg width="14" height="14" viewBox="0 0 14 14"><circle cx="6" cy="6" r="4.5" fill="none" stroke="#444" stroke-width="1.6"/><line x1="9.3" y1="9.3" x2="13" y2="13" stroke="#444" stroke-width="1.8"/></svg>
    </div>
    <div class="contact">
      <span><svg width="26" height="18" viewBox="0 0 26 18"><rect x="1" y="1" width="24" height="16" fill="none" stroke="#5b2c0a" stroke-width="2"/><polyline points="1,1 13,10 25,1" fill="none" stroke="#5b2c0a" stroke-width="2"/></svg>info@calmhaven.example</span>
      <span><svg width="20" height="20" viewBox="0 0 20 20"><path d="M4 2l4 4-2 2c1 3 3 5 6 6l2-2 4 4-3 3C8 18 2 12 1 5z" fill="none" stroke="#5b2c0a" stroke-width="2"/></svg>10 20 30 40 50</span>
    </div>
    <nav class="nav">
      <a class="active" href="#">Home</a>
      <a href="#">About Us</a>
      <a href="#">Services Provided</a>
      <a href="#">Patient Resources</a>
      <a href="#">FAQ</a>
      <a href="#">Contact Us</a>
    </nav>
  </header>

  <section class="hero" role="img" aria-label="Photo of a family holding hands walking on a beach at the shoreline">
    <h2 class="hero-title">A PROFESSIONAL MEDICAL CORPORATION.</h2>
  </section>
  <a class="btn hero-btn" href="#">REQUEST AN APPOINTMENT</a>
  <div class="dots hero-dots"><i></i><i></i><i class="on"></i><i></i></div>

  <section class="welcome">
    <h1>Welcome to <strong>CALM HAVEN</strong></h1>
    <p>Lorem ipsum dolor sit amet, consectetuer adipiscing elit, sed diam nonummy nibh euismod tincidunt ut laoreet dolore magna aliquam erat volutpat.</p>
    <p>Ut wisi enim ad minim veniam, quis nostrud exerci tation ullamcorper suscipit lobortis nisl ut aliquip ex ea commodo consequat.</p>
    <p>Duis autem vel eum iriure dolor in hendrerit in vulputate velit esse molestie consequat, vel illum dolore eu feugiat nulla facilisis at vero eros et accumsan et iusto odio dignissim qui blandit praesent luptatum zzril delenit augue duis dolore te feugait nulla facilisi.</p>
  </section>

  <section class="appointment">
    <h2>APPOINTMENT</h2>
    <div class="field">NAME<svg width="14" height="14" viewBox="0 0 14 14"><circle cx="7" cy="4" r="3.5" fill="#c4c4c4"/><path d="M0 14c0-5 14-5 14 0z" fill="#c4c4c4"/></svg></div>
    <div class="field">EMAIL<svg width="18" height="12" viewBox="0 0 18 12"><rect x=".5" y=".5" width="17" height="11" fill="none" stroke="#c4c4c4"/><polyline points=".5,.5 9,7 17.5,.5" fill="none" stroke="#c4c4c4"/></svg></div>
    <div class="field message">MESSAGE<svg width="16" height="14" viewBox="0 0 16 14"><path d="M0 0h16v10H6l-4 4v-4H0z" fill="#c4c4c4"/></svg></div>
    <a class="btn send" href="#">SEND</a>
  </section>

  <section class="news">
    <h2>NEWS FEED</h2>
    <div class="dots news-dots"><i></i><i></i><i class="on"></i><i></i></div>
    <div class="card card-1" role="img" aria-label="Photo of a group of people seated in a row at a meeting"></div>
    <div class="card card-2" role="img" aria-label="Photo of caring hands in soft green tones">
      <svg width="38" height="38" viewBox="0 0 38 38"><circle cx="22" cy="16" r="13" fill="none" stroke="#fff" stroke-width="2"/><line x1="13" y1="25" x2="2" y2="36" stroke="#fff" stroke-width="2.5"/><line x1="22" y1="10" x2="22" y2="22" stroke="#fff" stroke-width="2"/><line x1="16" y1="16" x2="28" y2="16" stroke="#fff" stroke-width="2"/></svg>
      <h3>Lorem ipsum dolor</h3>
      <p>Consectetuer adipiscing elit, sed diam nonummy nibh euismod tincidunt ut laoreet dolore magna aliquam erat volutpat.</p>
    </div>
    <div class="card card-3" role="img" aria-label="Photo of a stressed woman at a desk beside a laptop"></div>
  </section>

  <footer class="footer">
    Copyright © 2014 Calm Haven Inc.
    <div class="social"><i></i><i></i><i></i></div>
  </footer>
</body>
</html>
```